Flyer für eine Tagespflege (Senioren & Demenzkranke)
Zielgruppe
Hallo wir sind eine Tagespflege die 365 Tage im Jahr geöffnet hat. Wir kümmern uns um Senioren und Demenzkranke. Zielgruppe sind Personen die Ihre Angehörigen (zur Entlastung) Zuhause pflegen und Senioren die den Tag in Gemeinschaft verbringen wollen und abends zu Hause im eigenen Bett schlafen wollen
Aufgabenstellung
Es sollte ansprechend bzw. hochwertig aussehen. Es sollte ein Standard Format sein. Bei der Größe gibt es keine Vorgabe. Es sollte übersichtlich sein. Die Adresse sollte mit Karte dargestellt sein. Das wir 365 Tage im Jahr geöffnet haben muss klar hervor gehen.

```html
<!DOCTYPE html>
<html lang="de">
<head>
<meta charset="utf-8">
<title>Tagespflege Lindenhof – Faltblatt</title>
<link href="https://fonts.googleapis.com/css2?family=Open+Sans:ital,wght@0,400;0,600;0,700;1,400;1,600&family=Libre+Baskerville:wght@700&display=swap" rel="stylesheet">
<style>
  :root{
    --page-bg:#e6ecee;
    --paper:#f7f7f6;
    --paper-grey:#e2e2e1;
    --olive:#b9aa4d;
    --olive-light:#dcd071;
    --olive-label:#d2c46a;
    --cream:#f3ecc0;
    --text:#3a3a3a;
    --text-soft:#555;
  }
  *{box-sizing:border-box;margin:0;padding:0}
  html,body{width:1200px;height:900px;overflow:hidden}
  body{background:var(--page-bg);font-family:"Open Sans",Arial,sans-serif;color:var(--text);position:relative}
  .spread{position:absolute;left:300px;width:600px;height:420px;display:flex;box-shadow:0 6px 18px rgba(0,0,0,.18)}
  .spread--outside{top:20px}
  .spread--inside{top:460px}
  .panel{position:relative;width:200px;height:420px;background:var(--paper);overflow:hidden}
  .panel + .panel{border-left:1px solid rgba(0,0,0,.06)}
  .panel--grey{background:linear-gradient(180deg,var(--paper) 0%,var(--paper-grey) 100%)}
  .top-rule{position:absolute;top:0;left:0;right:0;height:3px;background:var(--olive-light)}
  .blob{position:absolute;left:0;top:0;display:block}
  .rule{position:absolute;height:3px;background:var(--olive-light)}
  .quote{position:absolute;left:10px;right:10px;top:142px;text-align:center;font-style:italic;font-size:8px;line-height:1.3;color:var(--text-soft)}
  .brand{position:absolute;left:0;right:0;top:26px;display:flex;align-items:center;justify-content:center;gap:5px;font-weight:600;font-size:8px;color:var(--text-soft)}
  .brand__dot{width:6px;height:6px;border-radius:50%;background:var(--olive)}
  .brand--cover{left:auto;right:10px;top:22px;color:#fff}
  .intro{position:absolute;left:8px;right:8px;top:141px;text-align:center;font-size:8.4px;line-height:1.22;color:var(--text-soft)}
  .contact{position:absolute;left:0;right:0;top:336px;text-align:center;font-size:6.4px;line-height:1.3;color:var(--text)}
  .contact p + p{margin-top:7px}
  .cover-title{position:absolute;left:30px;top:330px;color:var(--cream);font-weight:600;font-size:10px;line-height:1.3}
  .cover-sub{display:block;margin-top:4px;font-size:6.6px;font-style:italic;font-weight:600}
  .label{position:absolute;left:12px;background:var(--olive-label);color:#fff;font-family:"Libre Baskerville",Georgia,serif;font-size:6.4px;letter-spacing:.06em;padding:6px 7px}
  .copy{position:absolute;left:12px;right:8px;font-size:7.6px;line-height:1.28;color:var(--text)}
  .copy p + p{margin-top:8px}
  .copy strong{font-weight:700}
</style>
</head>
<body>

<section class="spread spread--outside">
  <div class="panel">
    <div class="top-rule"></div>
    <div class="rule" style="left:34px;width:130px;top:130px"></div>
    <p class="quote">Glücklich ist der Mensch,<br>der seinen Nächsten trägt<br>in seiner ganzen Gebrechlichkeit<br>wie er sich wünscht,<br>von jenen getragen zu werden<br>in seiner ganzen Schwäche<br>(Hildegard Sommer)</p>
    <svg class="blob" width="200" height="420" role="img" aria-label="Foto: Seniorin liest mit einer Pflegekraft am Tisch die Zeitung">
      <defs><linearGradient id="gPaper" x1="0" y1="0" x2="1" y2="1"><stop offset="0" stop-color="#d9cfb6"/><stop offset=".6" stop-color="#c7c0b0"/><stop offset="1" stop-color="#a9b0a6"/></linearGradient></defs>
      <path d="M0,420 L0,318 C35,300 80,300 125,284 C165,270 188,276 196,320 C202,360 196,400 192,420 Z" fill="url(#gPaper)"/>
    </svg>
  </div>

  <div class="panel">
    <div class="top-rule"></div>
    <div class="brand"><span class="brand__dot"></span>Tagespflege Lindenhof</div>
    <div class="rule" style="left:30px;width:140px;top:128px"></div>
    <p class="intro">Sie möchten weiterhin in Ihrem Zuhause leben, Selbstbestimmung und Lebensqualität genießen und benötigen dabei Unterstützung? Gemeinsam mit Ihnen besprechen wir ein für Sie passendes Leistungs- und Serviceangebot nach Ihren Wünschen und Bedürfnissen.</p>
    <div class="contact">
      <p>Kontakt / Adresse</p>
      <p>Tagespflege<br>Marta Keller<br>Birkenweg 14<br>17000 Mühlental</p>
      <p>Telefon 04567/1234567<br>E-Mail kontakt@tagespflege-lindenhof.de</p>
    </div>
  </div>

  <div class="panel">
    <svg class="blob" width="200" height="420" role="img" aria-label="Foto: Pflegekraft reicht einer Seniorin lächelnd eine Tasse">
      <defs><linearGradient id="gCover" x1="0" y1="0" x2="1" y2="1"><stop offset="0" stop-color="#a7c98a"/><stop offset=".45" stop-color="#9fb3c6"/><stop offset="1" stop-color="#5f7a5a"/></linearGradient></defs>
      <rect width="200" height="420" fill="url(#gCover)"/>
    </svg>
    <div class="brand brand--cover">Tagespflege Lindenhof</div>
    <svg class="blob" width="200" height="420" aria-hidden="true">
      <path d="M0,420 L0,340 C6,290 45,262 100,266 C150,270 185,292 200,305 L200,420 Z" fill="var(--olive)"/>
    </svg>
    <p class="cover-title">Tagespflege des<br>Ambulanten Pflegedienstes<span class="cover-sub">365 Tage Betreuung</span></p>
  </div>
</section>

<section class="spread spread--inside">
  <div class="panel">
    <svg class="blob" width="200" height="420" role="img" aria-label="Foto: Pflegekraft im Gespräch mit einem Senior im Garten">
      <defs><linearGradient id="gGarden" x1="0" y1="0" x2="1" y2="1"><stop offset="0" stop-color="#8fb36f"/><stop offset=".6" stop-color="#6f8a62"/><stop offset="1" stop-color="#b9ab98"/></linearGradient></defs>
      <path d="M0,0 L180,0 C204,40 204,110 182,130 C150,148 108,116 58,124 C28,128 10,136 0,142 Z" fill="url(#gGarden)"/>
    </svg>
    <span class="label" style="top:150px">UNSERE TAGESPFLEGE</span>
    <div class="copy" style="top:176px">
      <p>Sie fühlen sich in Ihrem Zuhause wohl möchten oder können dort aber nicht den gesamten Tag über alleine sein? Unsere Tagespflege bietet Ihnen behaglich eingerichtete Räumlichkeiten, nette Gesellschaft und Abwechslung.</p>
      <p>Als <strong>Tagesgast</strong> in unserer 2017 eröffneten Einrichtung erwartet Sie hier täglich wechselnde sinnvolle <strong>Betreuungsangebote</strong> mit verschiedenen Aktivitäten, die auf jeden Tagesgast <strong>individuell abgestimmt</strong> sind. Das abwechslungsreiche Freizeitprogramm können Sie nach Ihren Wünschen wahrnehmen oder sich zwischendurch zurückziehen und Abgeschiedenheit und Ruhe genießen.</p>
      <p>Unsere Tagespflege ist als einzige in Mühlental an <strong>365 Tagen im Jahr geöffnet</strong>!</p>
    </div>
  </div>

  <div class="panel panel--grey">
    <div class="top-rule"></div>
    <span class="label" style="top:48px">LEISTUNGEN</span>
    <div class="copy" style="top:78px">
      <p>Mit unserer Tagespflege schließen wir die Lücke zwischen <strong>Häuslichkeit</strong> und <strong>Pflegeheim</strong>.</p>
      <p>Wir unterstützen unsere Gäste dabei, im Rahmen ihrer individuellen Fähigkeiten und Wünsche <strong>selbstbestimmt</strong> am Leben teilzunehmen und <strong>aktiv</strong> zu sein.<br>Ihre Angehörigen werden gleichzeitig entlastet und können in Ruhe arbeiten. Besuchen Sie unser Gästehaus und schauen Sie sich um.</p>
      <p>Im <strong>persönlichen Gespräch</strong> beraten wir Sie vor Ort zu unseren Leistungen. Auf Wunsch vereinbaren Sie einen Termin. Gern können Sie dann, für ihren Angehörigen einen <strong>kostenlosen Schnuppertag</strong> in unserer Tagespflege festlegen.</p>
    </div>
    <svg class="blob" width="200" height="420" role="img" aria-label="Foto: heller Aufenthaltsraum mit Küche und Esstischen">
      <defs><linearGradient id="gRoom" x1="0" y1="0" x2="1" y2="1"><stop offset="0" stop-color="#efd9b0"/><stop offset=".5" stop-color="#e6c99a"/><stop offset="1" stop-color="#b8a489"/></linearGradient></defs>
      <path d="M8,302 C55,296 120,306 175,294 C195,290 198,320 194,350 C190,385 194,405 197,420 L12,420 C3,385 2,340 8,302 Z" fill="url(#gRoom)"/>
    </svg>
  </div>

  <div class="panel">
    <div class="top-rule"></div>
    <svg class="blob" width="200" height="420" role="img" aria-label="Fotos: Gesellschaftsspiel mit Spielfiguren und ein Teller mit frischem Obst">
      <defs>
        <linearGradient id="gGame" x1="0" y1="0" x2="1" y2="1"><stop offset="0" stop-color="#e6d3b6"/><stop offset="1" stop-color="#c9a97a"/></linearGradient>
        <linearGradient id="gFruit" x1="0" y1="0" x2="1" y2="1"><stop offset="0" stop-color="#f0e2a4"/><stop offset=".5" stop-color="#e8b66e"/><stop offset="1" stop-color="#d99a8a"/></linearGradient>
      </defs>
      <path d="M6,4 L90,4 L88,88 C70,94 45,84 25,90 C13,93 6,86 6,78 Z" fill="url(#gGame)"/>
      <path d="M95,4 L200,2 L200,88 C175,80 150,86 122,88 C103,90 95,82 95,70 Z" fill="url(#gFruit)"/>
    </svg>
    <span class="label" style="top:128px">UNSER TEAM</span>
    <div class="copy" style="top:155px">
      <p>Das Team der Tagespflege besteht aus <strong>12 erfahrenen und hoch motivierten Mitarbeitern</strong>, die sich um Ihr Wohl kümmern.</p>
      <p>Auf Wunsch holen wir Sie morgens zu Hause ab und bringen Sie am Nachmittag zurück.<br>Bei der Betreuung und Tagesgestaltung stehen Ihre <strong>individuellen Wünsche</strong> und <strong>Fähigkeiten</strong> an erster Stelle. Gemeinsame Ausflüge, Bewegungsübungen, Spiele oder Kochen sorgen für <strong>Abwechslung plus Spaß</strong> und lassen keinen Tag lang werden.</p>
    </div>
    <svg class="blob" width="200" height="420" role="img" aria-label="Foto: das Team der Tagespflege draußen im Grünen">
      <defs><linearGradient id="gTeam" x1="0" y1="0" x2="1" y2="1"><stop offset="0" stop-color="#8fb46f"/><stop offset=".6" stop-color="#5f7f55"/><stop offset="1" stop-color="#8c8e86"/></linearGradient></defs>
      <path d="M4,420 C0,380 2,330 26,304 C52,280 95,288 140,294 C175,298 194,290 200,292 L200,420 Z" fill="url(#gTeam)"/>
    </svg>
  </div>
</section>

</body>
</html>
```